Packaging Design Project

We are creating a twin aluminium foil pack. I have posted up two pictures.

Picture 1 is each packet front and back with the dimensions BUT remember this is a twin pack so on picture 2 you will see how they are joined together.

You will insert our company logo ( picture 3) onto each pack ( small version on the top left hand side of each)

You will design another logo for the name Tessa Glow and insert it along the top of each pack in the centre.

We will retain the red black theme as per photo 2 and retain the numbers 1 and 2 as per the photos.

On pack numbered 1 the front wording will be "Duro Prepwash"

The instructions on the back rear of number 1 is as follows

1) Remove Duro Prepwash from package
2) Thoroughly wipe screen surface to remove dirt, oil and other impurities and leave for 5 minutes to dry.
(Insert a warning sign picture)

Inflammable. Keep out of reach of children. Keep away from sources of ignition- In case of contact with eyes rinse immediatley with plenty of water and seek medical advice.If swallowed, seek immediate medical advice and show this container or label

On pack number 2 the front wording will be "Tessa Glow"

The instructions on the back rear of number two is as follows

1) Remove Tessa Glow from package
2) Thoroughly apply Tessa Glow to your devices screen and leave to dry for 5 minutes.
3) Tessa Glow is now reacting with oxygen to apply a Nano glass shield on your device. After 30 minutes, wipe screen with cloth till clean.
4) Your device is now fully protected for up to three months and ready for use.

Target Market(s)

customers who use screen protectors for olvos, tablets and smart phones

Industry/Entity Type

Medical

Requirements
Must have
• Must supply full Ai, jpg and gif files with this project
Nice to have

```html
<!DOCTYPE html>
<html lang="en">
<head>
<meta charset="utf-8">
<title>Tessa Glow twin pack</title>
<link rel="stylesheet" href="https://fonts.googleapis.com/css2?family=Bodoni+Moda:wght@400&family=PT+Sans:wght@400&display=swap">
<style>
  :root {
    --stage: #e6e7e8;
    --sheet: #ffffff;
    --red: #ed1c24;
    --black: #0b0b0b;
    --ink-light: #ffffff;
    --ink-dark: #1a1a1a;
    --fold: #ed1c24;
  }
  * { box-sizing: border-box; margin: 0; padding: 0; }
  html, body { width: 1200px; height: 1200px; overflow: hidden; }
  body {
    background: var(--stage);
    font-family: "PT Sans", sans-serif;
    position: relative;
  }
  .sheet {
    position: absolute;
    left: 183px;
    width: 832px;
    height: 500px;
    background: var(--sheet);
  }
  .sheet--front { top: 54px; }
  .sheet--back { top: 635px; }
  .fold-line {
    position: absolute;
    left: 415px;
    top: 0;
    height: 100%;
    border-left: 2px dashed var(--fold);
  }
  .pack {
    position: absolute;
    top: 42px;
    width: 333px;
    height: 416px;
    border-radius: 22px;
    color: var(--ink-light);
    overflow: hidden;
  }
  .pack--left { left: 43px; }
  .pack--right { left: 459px; }
  .pack--red { background: var(--red); }
  .pack--black { background: var(--black); }

  .pack-header {
    position: absolute;
    top: 12px;
    left: 12px;
    right: 16px;
    height: 52px;
  }
  .company-mark {
    position: absolute;
    left: 0;
    top: 2px;
    display: flex;
    flex-direction: column;
    align-items: center;
    gap: 3px;
    font-size: 13px;
    line-height: 1;
    color: var(--ink-light);
  }
  .company-mark__dot {
    width: 20px;
    height: 20px;
    border-radius: 50%;
    background: var(--ink-light);
  }
  .pack--red .company-mark { color: var(--black); }
  .pack--red .company-mark__dot { background: var(--black); }
  .product-mark {
    position: absolute;
    left: 60px;
    right: 0;
    top: 10px;
    text-align: center;
    font-size: 22px;
    line-height: 24px;
    color: var(--ink-light);
  }

  .pack-number {
    position: absolute;
    left: 0;
    right: 0;
    top: 70px;
    text-align: center;
    font-family: "Bodoni Moda", serif;
    font-size: 300px;
    line-height: 300px;
    color: var(--ink-light);
  }
  .pack-name {
    position: absolute;
    left: 0;
    right: 0;
    bottom: 22px;
    text-align: center;
    font-size: 33px;
  }
  .pack--red .pack-name { color: var(--ink-dark); }

  .steps {
    position: absolute;
    font-size: 14px;
    line-height: 17px;
    list-style: none;
  }
  .steps li { display: flex; gap: 8px; }
  .steps li + li { margin-top: 1px; }
  .steps--long { left: 22px; top: 90px; width: 300px; }
  .steps--short { left: 72px; top: 108px; width: 190px; }

  .warning {
    position: absolute;
    left: 12px;
    right: 8px;
    top: 262px;
    font-size: 13px;
    line-height: 16px;
  }
  .warning__icon { display: block; width: 32px; height: 28px; margin-bottom: 6px; }
</style>
</head>
<body>

<section class="sheet sheet--front">
  <div class="fold-line"></div>

  <article class="pack pack--left pack--red">
    <header class="pack-header">
      <div class="company-mark"><span class="company-mark__dot"></span>Pelto</div>
      <div class="product-mark">Tessa Glow</div>
    </header>
    <div class="pack-number">1</div>
    <div class="pack-name">Duro Prepwash</div>
  </article>

  <article class="pack pack--right pack--black">
    <header class="pack-header">
      <div class="company-mark"><span class="company-mark__dot"></span>Pelto</div>
      <div class="product-mark">Tessa Glow</div>
    </header>
    <div class="pack-number">2</div>
    <div class="pack-name">Tessa Glow</div>
  </article>
</section>

<section class="sheet sheet--back">
  <div class="fold-line"></div>

  <article class="pack pack--left pack--black">
    <header class="pack-header">
      <div class="company-mark"><span class="company-mark__dot"></span>Pelto</div>
      <div class="product-mark">Tessa Glow</div>
    </header>
    <ol class="steps steps--long">
      <li><span>1)</span><span>Remove Tessa Glow from package</span></li>
      <li><span>2)</span><span>Thoroughly apply Tessa Glow to your devices screen and leave to dry for 5 minutes.</span></li>
      <li><span>3)</span><span>Tessa Glow is now reacting with oxygen to apply a Nano glass shield on your device. After 30 minutes, wipe screen with cloth till clean.</span></li>
      <li><span>4)</span><span>Your device is now fully protected for up to three months and ready for use.</span></li>
    </ol>
    <div class="warning">
      <svg class="warning__icon" viewBox="0 0 32 28" aria-hidden="true">
        <path d="M16 2 L30 26 H2 Z" fill="#ffffff" stroke="#ed1c24" stroke-width="3" stroke-linejoin="round"/>
        <rect x="14.6" y="10" width="2.8" height="9" fill="#0b0b0b"/>
        <rect x="14.6" y="20.5" width="2.8" height="2.8" fill="#0b0b0b"/>
      </svg>
      <p>Inflammable. Keep out of reach of children. Keep away from sources of ignition- In case of contact with eyes rinse immediatley with plenty of water and seek medical advice.If swallowed, seek immediate medical advice and show this container or label</p>
    </div>
  </article>

  <article class="pack pack--right pack--red">
    <header class="pack-header">
      <div class="company-mark"><span class="company-mark__dot"></span>Pelto</div>
      <div class="product-mark">Tessa Glow</div>
    </header>
    <ol class="steps steps--short">
      <li><span>1)</span><span>Remove Duro Prepwash from package</span></li>
      <li><span>2)</span><span>Thoroughly wipe screen surface to remove dirt, oil and other impurities and leave for 5 minutes to dry.</span></li>
    </ol>
    <div class="warning">
      <svg class="warning__icon" viewBox="0 0 32 28" aria-hidden="true">
        <path d="M16 2 L30 26 H2 Z" fill="#ffffff" stroke="#0b0b0b" stroke-width="3" stroke-linejoin="round"/>
        <rect x="14.6" y="10" width="2.8" height="9" fill="#0b0b0b"/>
        <rect x="14.6" y="20.5" width="2.8" height="2.8" fill="#0b0b0b"/>
      </svg>
      <p>Inflammable. Keep out of reach of children. Keep away from sources of ignition- In case of contact with eyes rinse immediatley with plenty of water and seek medical advice.If swallowed, seek immediate medical advice and show this container or label</p>
    </div>
  </article>
</section>

</body>
</html>
```